Hip-Hop Artist RT Marble new album cover design for "Quiet Engines"

Artist: RT Marble
Album Title: Quiet Engines
I am attaching a un-edited picture to use & some sample images with the "Quiet Engines" concept directions. I am hoping that the graphic designers accepting this challenge can do a better or different job than the 3 sample design images attached. I do like each of the 3 attached drafts(Draft, Draft2, Draft3) concepts. But, would like to see other creative design approaches and other possible affect. artwork ideas.
I am also attaching a number of random design that I also like the direction on.
Please let em know if you have any questions, and I will respond as quickly as possible.

```html
<!DOCTYPE html>
<html lang="en">
<head>
<meta charset="utf-8">
<title>RT Marble — Quiet Engines</title>
<link rel="stylesheet" href="https://fonts.googleapis.com/css2?family=Permanent+Marker&display=swap">
<style>
  :root {
    --floor-dark: #0b0d10;
    --floor-mid: #23272c;
    --floor-light: #3a3f45;
    --paper: #e9ebee;
    --paper-shade: #9ea3a9;
    --ink-yellow: #f2ae1c;
    --ink-yellow-soft: #d9981a;
  }
  html, body {
    margin: 0;
    padding: 0;
    width: 1200px;
    height: 1200px;
    overflow: hidden;
    background: var(--floor-dark);
  }
  .album-cover {
    position: relative;
    width: 1200px;
    height: 1200px;
    overflow: hidden;
  }
  .album-cover svg {
    display: block;
    width: 1200px;
    height: 1200px;
  }
  .ring-text {
    font-family: "Permanent Marker", "Comic Sans MS", cursive;
    fill: var(--ink-yellow);
    text-transform: uppercase;
  }
  .ring-text--soft { fill: var(--ink-yellow-soft); }
  .ring-text--small { font-size: 26px; letter-spacing: 6px; }
  .ring-text--medium { font-size: 36px; letter-spacing: 8px; }
  .ring-text--large { font-size: 50px; letter-spacing: 10px; }
</style>
</head>
<body>
<main class="album-cover">
  <svg viewBox="0 0 1200 1200" xmlns="http://www.w3.org/2000/svg">
    <defs>
      <radialGradient id="floor-light" cx="600" cy="640" r="900" gradientUnits="userSpaceOnUse">
        <stop offset="0" stop-color="var(--floor-light)"/>
        <stop offset="0.45" stop-color="var(--floor-mid)"/>
        <stop offset="1" stop-color="var(--floor-dark)"/>
      </radialGradient>
      <radialGradient id="paper-pool" cx="600" cy="640" r="300" gradientUnits="userSpaceOnUse">
        <stop offset="0" stop-color="#15171a"/>
        <stop offset="0.42" stop-color="#2a2d31"/>
        <stop offset="0.6" stop-color="var(--paper-shade)"/>
        <stop offset="0.8" stop-color="var(--paper)"/>
        <stop offset="1" stop-color="var(--paper-shade)"/>
      </radialGradient>

      <path id="ring-330" d="M270,640 a330,330 0 1,1 660,0 a330,330 0 1,1 -660,0"/>
      <path id="ring-372" d="M228,640 a372,372 0 1,1 744,0 a372,372 0 1,1 -744,0"/>
      <path id="ring-420" d="M180,640 a420,420 0 1,1 840,0 a420,420 0 1,1 -840,0"/>
      <path id="ring-468" d="M132,640 a468,468 0 1,1 936,0 a468,468 0 1,1 -936,0"/>
      <path id="ring-512" d="M88,640 a512,512 0 1,1 1024,0 a512,512 0 1,1 -1024,0"/>
      <path id="ring-562" d="M38,640 a562,562 0 1,1 1124,0 a562,562 0 1,1 -1124,0"/>
      <path id="ring-616" d="M-16,640 a616,616 0 1,1 1232,0 a616,616 0 1,1 -1232,0"/>
      <path id="ring-664" d="M-64,640 a664,664 0 1,1 1328,0 a664,664 0 1,1 -1328,0"/>
      <path id="ring-720" d="M-120,640 a720,720 0 1,1 1440,0 a720,720 0 1,1 -1440,0"/>
      <path id="ring-780" d="M-180,640 a780,780 0 1,1 1560,0 a780,780 0 1,1 -1560,0"/>
      <path id="ring-840" d="M-240,640 a840,840 0 1,1 1680,0 a840,840 0 1,1 -1680,0"/>
    </defs>

    <rect class="floor" width="1200" height="1200" fill="url(#floor-light)"/>

    <g class="title-rings">
      <text class="ring-text ring-text--small" transform="rotate(-20 600 640)"><textPath href="#ring-330">Quiet Engines · RT Marble · Quiet Engines · RT Marble · Quiet Engines · RT Marble ·</textPath></text>
      <text class="ring-text ring-text--small ring-text--soft" transform="rotate(35 600 640)"><textPath href="#ring-372">KVTEN · Quiet Engines · KVTEN · Quiet Engines · KVTEN · Quiet Engines · KVTEN ·</textPath></text>
      <text class="ring-text ring-text--large" transform="rotate(-70 600 640)"><textPath href="#ring-420">Quiet Engines · Quiet Engines · Quiet Engines · Quiet Engines ·</textPath></text>
      <text class="ring-text ring-text--small" transform="rotate(10 600 640)"><textPath href="#ring-468">RT Marble · Quiet Engines · KVTEN · RT Marble · Quiet Engines · KVTEN · RT Marble · Quiet Engines · KVTEN ·</textPath></text>
      <text class="ring-text ring-text--medium ring-text--soft" transform="rotate(55 600 640)"><textPath href="#ring-512">Quiet Engines · KVTEN · Quiet Engines · KVTEN · Quiet Engines · KVTEN · Quiet Engines ·</textPath></text>
      <text class="ring-text ring-text--large" transform="rotate(-40 600 640)"><textPath href="#ring-562">Quiet Engines · RT Marble · Quiet Engines · RT Marble · Quiet Engines ·</textPath></text>
      <text class="ring-text ring-text--medium" transform="rotate(80 600 640)"><textPath href="#ring-616">KVTEN · Quiet Engines · KVTEN · Quiet Engines · KVTEN · Quiet Engines · KVTEN · Quiet Engines · KVTEN ·</textPath></text>
      <text class="ring-text ring-text--large ring-text--soft" transform="rotate(-5 600 640)"><textPath href="#ring-664">Quiet Engines · Quiet Engines · Quiet Engines · Quiet Engines · Quiet Engines · Quiet Engines ·</textPath></text>
      <text class="ring-text ring-text--medium" transform="rotate(25 600 640)"><textPath href="#ring-720">RT Marble · Quiet Engines · KVTEN · RT Marble · Quiet Engines · KVTEN · RT Marble · Quiet Engines · KVTEN ·</textPath></text>
      <text class="ring-text ring-text--large" transform="rotate(-60 600 640)"><textPath href="#ring-780">Quiet Engines · KVTEN · Quiet Engines · KVTEN · Quiet Engines · KVTEN · Quiet Engines ·</textPath></text>
      <text class="ring-text ring-text--large ring-text--soft" transform="rotate(15 600 640)"><textPath href="#ring-840">Quiet Engines · RT Marble · Quiet Engines · RT Marble · Quiet Engines · RT Marble · Quiet Engines ·</textPath></text>
    </g>

    <circle class="artist-photo" cx="600" cy="640" r="300" fill="url(#paper-pool)"
            role="img" aria-label="Photo: the artist dressed in black, crouching on a dark stone floor surrounded by scattered sheets of paper, seen from above"/>
  </svg>
</main>
</body>
</html>
```